Sleek and Morden Business Card

Business Card Design for Business Name "Lantern Pine Services (LPS)"
Offering Virtual Assistant (VA) services including Virtual Receptionist, Appointment and Diary Management. Taking and Answering calls for Sole Trader Businesses. Quotes, Invoices, Expense Reconciliation, Accounts Payable and Accounts Receivable.
Lantern Services offers clients the ease of a complete office without the physical need to having an office.
Target Market(s)
Target market are Sole Traders like Electricians, Plumbers, Painters etc.
Industry/Entity Type
Business
Colors
Designer to choose colors to be used in the design.
Look and feel
Each slider illustrates characteristics of the customer's brand and the style your logo design should communicate.

```html
<!DOCTYPE html>
<html lang="en">
<head>
<meta charset="utf-8">
<title>Lantern Pine Services – Business Card</title>
<link rel="stylesheet" href="https://fonts.googleapis.com/css2?family=Dosis:wght@600&family=Jost:wght@500;600;700&display=swap">
<style>
  :root {
    --backdrop: #d9d8d5;
    --card: #3a3b3d;
    --card-deep: #2b2c2e;
    --accent: #8ae6ee;
    --ink-light: #ffffff;
  }
  * { margin: 0; padding: 0; box-sizing: border-box; }
  html, body { width: 1200px; height: 848px; overflow: hidden; }
  body { background: var(--backdrop); position: relative; font-family: "Jost", sans-serif; }

  .card {
    position: absolute;
    background: var(--card);
    overflow: hidden;
    box-shadow: 0 6px 18px rgba(0,0,0,0.35);
  }
  .card svg.arcs { position: absolute; inset: 0; }

  .card-front {
    left: 190px; top: 105px; width: 575px; height: 385px;
    border-bottom-left-radius: 120px;
  }
  .card-back {
    left: 418px; top: 382px; width: 595px; height: 380px;
    border-bottom-right-radius: 120px;
  }

  .brand-mark {
    position: absolute; left: 12px; top: 22px;
    font-weight: 600; font-size: 64px; letter-spacing: 2px;
    color: var(--card-deep); line-height: 1;
  }
  .holder-name {
    position: absolute;
    font-family: "Dosis", sans-serif; font-weight: 600;
    color: var(--accent); line-height: 1;
  }
  .card-front .holder-name { left: 0; width: 570px; text-align: center; top: 160px; font-size: 44px; }
  .business-name {
    position: absolute; left: 0; width: 575px; text-align: center; top: 226px;
    font-weight: 500; font-size: 18px; line-height: 1.2; color: var(--ink-light);
  }

  .service-line {
    position: absolute; right: 48px; top: 18px;
    font-weight: 700; font-size: 26px; color: var(--card-deep);
  }
  .card-back .holder-name { right: 40px; top: 122px; font-size: 46px; }
  .contact {
    position: absolute; right: 28px; top: 190px; text-align: right;
    color: var(--ink-light); font-weight: 500; font-size: 15px; line-height: 1;
  }
  .contact li { list-style: none; margin-bottom: 25px; }
  .contact li:nth-child(2) { margin-right: 8px; }
  .contact li:nth-child(1) { margin-right: 10px; }
  .contact .label { margin-right: 8px; }
</style>
</head>
<body>
  <section class="card card-front" aria-label="Card front">
    <svg class="arcs" width="575" height="385" viewBox="0 0 575 385" aria-hidden="true">
      <circle cx="575" cy="0" r="190" fill="none" stroke="var(--accent)" stroke-width="11"/>
      <circle cx="575" cy="0" r="124" fill="none" stroke="var(--ink-light)" stroke-width="6"/>
    </svg>
    <div class="brand-mark">LPS</div>
    <h1 class="holder-name">Mara Kellaway</h1>
    <p class="business-name">Lantern Pine Services</p>
  </section>

  <section class="card card-back" aria-label="Card back">
    <svg class="arcs" width="595" height="380" viewBox="0 0 595 380" aria-hidden="true">
      <circle cx="0" cy="20" r="190" fill="none" stroke="var(--accent)" stroke-width="11"/>
      <circle cx="0" cy="20" r="122" fill="none" stroke="var(--ink-light)" stroke-width="6"/>
    </svg>
    <p class="service-line">Virtual Assistant Services</p>
    <h2 class="holder-name">Mara Kellaway</h2>
    <ul class="contact">
      <li>Proprietor/Director</li>
      <li><span class="label">Mobile</span>0400 555 128</li>
      <li><span class="label">Email</span>mara@lanternpine.com.au</li>
    </ul>
  </section>
</body>
</html>
```